OLVAK Web Design (Need help to re-design our website)

We need someone to help us re-design our website and launch it. All contents for the website are ready. (https://olvak.example.au/)

-Rearrange categories:
1. Heating & Cooling
2. Remove Home Appliance
3. Remove Entertainment

Home page - redesign (It will be a nice touch if the banner is in the loop).

NOTE:
-Brand colour blue and orange.
-Try using professional fonts (Example: Helvetica, etc.)
-The website's Footer should be readable and use light colour.

Target Market(s)

Residentials & commercial buildings

Industry/Entity Type

Heat Ventilation and Cooling Industry, Technology , Renewables

Coding

Coded - Design and coding required

Colors
0094D4
00A9DD
6FCCEA
C7EBF8
E9F6FB
59FF00
82FF00
B8FF75
E3FFCB
F4FFEA
F0912C
F2A743
F7CA91
FBE8D2
FDF5EE

Requirements
Nice to have
• Effects/transition on the words/copy/images.

```html
<!DOCTYPE html>
<html lang="en">
<head>
<meta charset="utf-8">
<title>OLVAK – Heating &amp; Cooling</title>
<link rel="stylesheet" href="https://fonts.googleapis.com/css2?family=Outfit:wght@300;400;500;600;700&display=swap">
<style>
:root{
  --blue:#1a5aab;
  --navy:#123f78;
  --deep:#0c2f5c;
  --orange:#f7931e;
  --text:#222;
  --muted:#555;
  --line:#e6e6e6;
  --soft:#f2f2f4;
  --white:#fff;
}
*{box-sizing:border-box;margin:0;padding:0}
html,body{width:1200px;height:2755px;overflow:hidden}
body{font-family:"Outfit",Helvetica,Arial,sans-serif;color:var(--text);background:var(--white);position:relative}
.abs{position:absolute}
.topbar{left:0;top:0;width:1200px;height:36px;background:var(--navy);color:#fff;font-size:13px}
.topbar .promo{left:86px;top:10px}
.topbar .promo b{font-weight:600}
.topbar .addr{left:748px;top:9px;font-size:14px;display:flex;gap:8px;align-items:center}
.topbar .soc{top:0;width:36px;height:36px;background:var(--blue);display:flex;align-items:center;justify-content:center}
.topbar .soc span{width:16px;height:16px;border-radius:50%;background:#fff}
.header{left:0;top:36px;width:1200px;height:86px;border-bottom:1px solid var(--line)}
.brand{font-weight:700;font-size:38px;letter-spacing:5px;color:var(--blue);display:flex;align-items:center;gap:12px}
.brand i{width:34px;height:34px;border-radius:50%;background:var(--orange);display:block}
.header .brand{left:86px;top:18px}
.search{left:321px;top:24px;width:338px;height:34px;border:1px solid #ccc;border-radius:18px;overflow:hidden}
.search span{position:absolute;left:18px;top:8px;font-size:13px;color:#666}
.search b{position:absolute;right:0;top:0;width:52px;height:34px;background:var(--orange);display:flex;align-items:center;justify-content:center}
.staff{left:688px;top:20px;text-align:center;font-size:12px;color:#444}
.contact{top:22px;display:flex;gap:10px;align-items:center;font-size:15px;font-weight:500;line-height:1.15}
.contact .ic{width:38px;height:38px;border-radius:50%;background:var(--blue);display:flex;align-items:center;justify-content:center}
.contact em{font-style:normal;color:var(--blue)}
.nav{left:0;top:122px;width:1200px;height:48px;font-size:16px;font-weight:500}
.nav a{position:absolute;top:14px;color:var(--text);text-decoration:none}
.nav .book{left:943px;top:0;width:171px;height:48px;background:var(--orange);color:#fff;display:flex;align-items:center;justify-content:center}
.hero{left:0;top:170px;width:1200px;height:420px;background:linear-gradient(90deg,#0e3a6e 0%,#1a4c82 35%,#8c7c6c 55%,#c9b8a4 75%,#e6dfd6 100%);overflow:hidden}
.hero-curve{right:-120px;top:-40px;width:470px;height:560px;border-radius:50%;background:#e9ecea;border-left:6px solid #fff}
.hero h1{left:86px;top:106px;color:#fff;font-weight:400;font-size:39px;line-height:46px}
.hero h1 .hl{color:var(--orange);font-weight:600}
.hero h1 .bd{font-weight:500}
.pill{background:var(--orange);color:#fff;font-size:16px;border-radius:30px 4px 30px 4px;display:flex;align-items:center;justify-content:center}
.hero .pill{left:86px;top:273px;width:150px;height:40px}
.dots{left:86px;top:362px;display:flex;gap:6px}
.dots i{width:6px;height:6px;border-radius:50%;background:#fff}
.dots i:first-child{background:var(--orange)}
.products{left:810px;top:205px;width:250px;height:418px;background:linear-gradient(90deg,#d7d9dc,#f7f7f7 40%,#dcdde0);border-radius:14px 14px 6px 6px;box-shadow:0 18px 20px -12px rgba(0,0,0,.45)}
.hblue{color:var(--blue)}
.horange{color:var(--orange)}
.offer h2{left:86px;top:688px;font-size:31px;line-height:37px;font-weight:600;color:var(--blue)}
.offer p{left:86px;top:818px;width:235px;font-size:15px;line-height:19px}
.offer .pill{left:86px;top:898px;width:150px;height:42px}
.card{top:696px;width:226px;height:244px;background:#fff;border-top:13px solid var(--orange);border-radius:10px;box-shadow:0 2px 8px rgba(0,0,0,.15);text-align:center}
.card .circ{width:74px;height:74px;border-radius:50%;background:var(--blue);margin:23px auto 12px;display:flex;align-items:center;justify-content:center}
.card h3{font-size:22px;font-weight:500;color:var(--blue);margin-bottom:12px}
.card p{font-size:13.5px;line-height:17px;color:#333;padding:0 22px}
.story-photo1{left:86px;top:1031px;width:315px;height:414px;border-radius:14px 130px 0 14px;background:linear-gradient(160deg,#c9cdd2,#2f64b5 55%,#5b5f66)}
.story-photo2{left:252px;top:1185px;width:314px;height:304px;border-radius:130px 14px 14px 14px;background:linear-gradient(135deg,#6b4a36,#b8b9b8 45%,#8f9291 70%,#4b6b35);border:6px solid #fff}
.dotgrid{left:360px;top:1060px;width:170px;height:120px;background-image:radial-gradient(#c8c8c8 1.4px,transparent 1.5px);background-size:16px 16px}
.eyebrow{font-size:16px;color:var(--orange);font-weight:400}
.story .eyebrow{left:630px;top:1047px}
.story h2{left:630px;top:1080px;font-size:32px;line-height:38px;font-weight:600;color:var(--blue)}
.rule{width:66px;height:3px;background:var(--orange)}
.story .rule{left:632px;top:1174px}
.story .body{left:632px;top:1201px;width:482px;font-size:14px;line-height:19.6px;text-align:justify}
.story .body p+p{margin-top:19px}
.story .pill{left:634px;top:1449px;width:150px;height:42px}
.svc .eyebrow{left:0;width:1200px;text-align:center;top:1597px}
.svc h2{left:0;width:1200px;text-align:center;top:1630px;font-size:32px;font-weight:600;color:var(--blue)}
.svc .rule{left:567px;top:1695px}
.tile{top:1740px;width:247px;height:367px;border-radius:12px;overflow:hidden}
.tile div{position:absolute;inset:0}
.tile span{position:absolute;left:0;right:0;bottom:22px;text-align:center;color:#fff;font-size:16px;font-weight:600}
.tile::after{content:"";position:absolute;left:0;right:0;bottom:0;height:150px;background:linear-gradient(transparent,#1a5aab)}
.tile span{z-index:2}
.foot-bg{left:0;top:2280px;width:1200px;height:423px;background:var(--soft);border-radius:500px 0 0 0}
.cta{left:171px;top:2177px;width:857px;height:208px;background:var(--orange);border-radius:200px 0 200px 0;color:#fff}
.cta .lead{left:83px;top:72px;font-size:25px;font-weight:600;line-height:30px}
.cta .dash{top:97px;width:42px;height:2px;background:#fff}
.cta .phone{left:422px;top:61px;width:72px;height:72px;border-radius:50%;background:#fff;display:flex;align-items:center;justify-content:center}
.cta .num{left:567px;top:60px;font-size:36px;font-weight:600;line-height:38px}
.cta .mail{left:567px;top:100px;font-size:24px;font-weight:600}
.footer .brand{left:86px;top:2440px;font-size:40px}
.footer .about{left:86px;top:2518px;width:280px;font-size:13.5px;line-height:20.5px;text-align:justify;letter-spacing:-.3px}
.fcol h4{font-size:22px;font-weight:500;color:var(--blue)}
.fcol .rule{width:38px;height:2px;margin:8px 0 16px}
.fcol li{list-style:none;font-size:14px;line-height:17px;margin-bottom:17px}
.fcol li.head{font-weight:600}
.fcol .gi{display:flex;gap:12px}
.fcol .gi i{width:9px;height:9px;border-radius:50%;background:var(--orange);margin-top:4px;flex:none}
.copy{left:0;top:2703px;width:1200px;height:52px;border-top:1px solid #ddd;background:var(--soft);text-align:center;font-size:14px;padding-top:17px}
</style>
</head>
<body>

<div class="abs topbar">
  <div class="abs promo">Don't miss our <b>Latest Promotions</b></div>
  <div class="abs addr"><svg width="14" height="16" viewBox="0 0 14 16"><path d="M7 0a6 6 0 0 0-6 6c0 4 6 10 6 10s6-6 6-10a6 6 0 0 0-6-6z" fill="#fff"/><circle cx="7" cy="6" r="2.3" fill="#123f78"/></svg>48 Harbour Rd, Eastvale VIC 3999</div>
  <div class="abs soc" style="left:1040px"><span></span></div>
  <div class="abs soc" style="left:1077px"><span style="border-radius:4px"></span></div>
</div>

<header class="abs header">
  <div class="abs brand"><i></i>OLVAK</div>
  <div class="abs search"><span>Search Products..</span><b><svg width="18" height="18" viewBox="0 0 18 18"><circle cx="7.5" cy="7.5" r="6" stroke="#fff" stroke-width="2" fill="none"/><path d="M12 12l5 5" stroke="#fff" stroke-width="2"/></svg></b></div>
  <div class="abs staff"><svg width="24" height="24" viewBox="0 0 24 24"><circle cx="12" cy="12" r="11" stroke="#f7931e" stroke-width="1.5" fill="none"/><circle cx="12" cy="9" r="4" stroke="#f7931e" stroke-width="1.5" fill="none"/><path d="M5 19c2-4 12-4 14 0" stroke="#f7931e" stroke-width="1.5" fill="none"/></svg><br>Staff Login</div>
  <div class="abs contact" style="left:780px"><span class="ic"><svg width="20" height="20" viewBox="0 0 20 20"><path d="M4 1l4 4-2 3c1 3 3 5 6 6l3-2 4 4-3 3C8 19 1 12 1 4z" fill="#fff"/></svg></span><div>Call Us on<br><em>18000 55210</em></div></div>
  <div class="abs contact" style="left:944px"><span class="ic"><svg width="20" height="16" viewBox="0 0 20 16"><rect x="1" y="2" width="18" height="12" rx="2" fill="#fff"/><path d="M2 3l8 6 8-6" stroke="#1a5aab" stroke-width="1.6" fill="none"/></svg></span><div>Mail Us on<br><em>info@olvak.example.au</em></div></div>
</header>

<nav class="abs nav">
  <a style="left:88px">Home</a>
  <a style="left:180px">Heating &amp; Cooling</a>
  <a style="left:365px">Our Story</a>
  <a style="left:488px">Support</a>
  <a style="left:749px">24h Emergency Services</a>
  <a class="book">Book Appointment</a>
</nav>

<section class="abs hero" role="img" aria-label="Family relaxing on a sofa in a comfortable living room">
  <div class="abs hero-curve"></div>
  <h1 class="abs">Revolutionise<br><span class="hl">Heating &amp; Cooling</span><br><span class="bd">Industry Australiawide</span></h1>
  <div class="abs pill">Explore Now</div>
  <div class="abs dots"><i></i><i></i><i></i></div>
</section>
<div class="abs products" role="img" aria-label="Two white heat pump water heater units"></div>

<section class="offer">
  <h2 class="abs">Offering<br><span class="horange">Solutions</span> for your<br>Requirements</h2>
  <p class="abs">Please select from a category below that best suits your requirements.</p>
  <div class="abs pill">Read More</div>
  <div class="abs card" style="left:402px"><div class="circ"><svg width="40" height="40" viewBox="0 0 40 40" fill="none" stroke="#fff" stroke-width="1.8"><path d="M4 20L20 6l16 14M9 16v18h22V16"/><rect x="16" y="24" width="8" height="10"/></svg></div><h3>Residential</h3><p>Offering complete solutions for your residential requirements.</p></div>
  <div class="abs card" style="left:644px"><div class="circ"><svg width="40" height="40" viewBox="0 0 40 40" fill="none" stroke="#fff" stroke-width="1.8"><path d="M6 12h20l-4-4M34 20H14l4 4M8 28l6 6h12l6-6"/></svg></div><h3>Trade</h3><p>Offering complete solutions for trade requirements.</p></div>
  <div class="abs card" style="left:887px"><div class="circ"><svg width="40" height="40" viewBox="0 0 40 40" fill="none" stroke="#fff" stroke-width="1.8"><rect x="8" y="8" width="12" height="26"/><rect x="20" y="14" width="12" height="20"/><path d="M11 13h6M11 18h6M11 23h6M23 19h6M23 24h6M4 34h32"/></svg></div><h3>Commercial</h3><p>Offering complete solutions for your business requirements.</p></div>
</section>

<section class="story">
  <div class="abs dotgrid"></div>
  <div class="abs story-photo1" role="img" aria-label="Technician in blue cap installing a wall air conditioner"></div>
  <div class="abs story-photo2" role="img" aria-label="Outdoor air conditioning condenser unit on grass"></div>
  <div class="abs eyebrow">OUR STORY</div>
  <h2 class="abs">We create the right climate and<br>temperature for your home</h2>
  <div class="abs rule"></div>
  <div class="abs body">
    <p>OLVAK is a company dedicated to manufacturing and installing energy-efficient products that reduce energy consumption, save costs, and promote sustainability. Our mission is to help individuals and businesses reduce their carbon footprint while also enhancing their comfort and quality of life.</p>
    <p>Our story began with a group of like-minded individuals who saw the urgent need to address climate change and the impact of energy consumption on the environment. We recognized that energy-efficient products were not only good for the planet but also for individuals' wallets. We believed that we could make a difference by developing and providing accessible and affordable energy-efficient solutions.</p>
  </div>
  <div class="abs pill">Read More</div>
</section>

<section class="svc">
  <div class="abs eyebrow">OUR SERVICES</div>
  <h2 class="abs">Specialist Heating &amp; Cooling Service</h2>
  <div class="abs rule"></div>
  <div class="abs tile" style="left:86px"><div role="img" aria-label="Heat pump water heater against a brick wall" style="background:linear-gradient(90deg,#9a6e55,#e6e8ea 35%,#f4f5f6 55%,#a7785c)"></div><span>Heat Pump</span></div>
  <div class="abs tile" style="left:346px"><div role="img" aria-label="Family under a wall air conditioner" style="background:linear-gradient(180deg,#dcdcda,#b8a996 50%,#8d8172)"></div><span>Air Conditioners</span></div>
  <div class="abs tile" style="left:606px"><div role="img" aria-label="Technician servicing a swimming pool heat pump" style="background:linear-gradient(180deg,#5d7a4a,#8fa07b 40%,#4c86b8 70%)"></div><span>Swimming Pool Heat Pump</span></div>
  <div class="abs tile" style="left:866px"><div role="img" aria-label="Monoblock heat pump unit outdoors" style="background:linear-gradient(180deg,#e8e8e6,#d2d3d0 55%,#6f8f4a)"></div><span>Monoblock Heat Pump</span></div>
</section>

<div class="abs foot-bg"></div>

<section class="abs cta">
  <div class="abs lead">Get your FREE<br>Repairing Consultation</div>
  <div class="abs dash" style="left:370px"></div>
  <div class="abs phone"><svg width="40" height="40" viewBox="0 0 20 20"><path d="M4 1l4 4-2 3c1 3 3 5 6 6l3-2 4 4-3 3C8 19 1 12 1 4z" fill="#f7931e"/></svg></div>
  <div class="abs dash" style="left:502px"></div>
  <div class="abs num">18000 55210</div>
  <div class="abs mail">info@olvak.example.au</div>
</section>

<footer class="footer">
  <div class="abs brand"><i></i>OLVAK</div>
  <p class="abs about">OLVAK is a company dedicated to manufacturing and installing energy-efficient products that reduce energy consumption, save costs, and promote sustainability. Our mission is to help individuals and businesses reduce their carbon footprint while also enhancing their comfort and quality of life.</p>
  <div class="abs fcol" style="left:439px;top:2448px"><h4>Our Products</h4><div class="rule"></div><ul>
    <li class="head">Heating &amp; Cooling</li><li>&gt;&nbsp; Heat Pump</li><li>&gt;&nbsp; Air Conditioners</li><li>&gt;&nbsp; Swimming Pool Heat Pump</li><li>&gt;&nbsp; Monoblock Heat Pump</li></ul></div>
  <div class="abs fcol" style="left:697px;top:2448px"><h4>Useful Links</h4><div class="rule"></div><ul>
    <li>&gt;&nbsp; Latest Promotions</li><li>&gt;&nbsp; Book Appointment</li><li>&gt;&nbsp; Privacy Policy</li><li>&gt;&nbsp; Terms &amp; Conditions</li><li>&gt;&nbsp; Sitemap</li></ul></div>
  <div class="abs fcol" style="left:916px;top:2448px"><h4>Get in Touch</h4><div class="rule"></div><ul>
    <li class="gi"><i></i><span>48 Harbour Rd, Eastvale<br>VIC 3999</span></li><li class="gi"><i></i>18000 55210</li><li class="gi"><i></i>info@olvak.example.au</li><li class="gi"><i></i>9AM - 5PM (Mon - Fri)</li></ul></div>
  <div class="abs copy">© Copyright 2024 OLVAK- All rights reserved.</div>
</footer>

</body>
</html>
```